Artificial intelligence, machine learning, and automation company needs a sexy business card design

We need a sleek and sexy business card design for an AI consulting company based in Philadelphia PA. We provide custom machine learning and automation solutions for companies of all shapes and sizes. The primary industries that we serve are pharmaceuticals, engineering, healthcare, and computer software. We would like the designs to be a black business card that uses green as a sleek accent color. The final design should communicate intelligence, cutting edge new-tech, and optimization.

Target Market(s)

C-level and VP level executives of multi-million annual companies. Mostly in Pharma, Healthcare, Real Estate, Retail, and Engineering

Industry/Entity Type

Computer Software

Contact Information for Business Card

Name: Jed Harlow
Title: CEO
Cell: 484 562 0937
Email: JedH@quillorbit.example
Website: www.QuillOrbit.example

Font styles to use
Sans Serif

Colors

Designer to choose colors to be used in the design.

Requirements
Must have
• 1) Attached Quillon Logo (either with colors or not/embossed)
• 2) "Artificial Intelligence" "Automation" and "Machine Learning"
• 3) "Quillon Laboratories" or "Quillon Labs" or "Quillon"
• 4) Sexy AF.
Nice to have
• Black card / dark card color, "Quillon Green" accent colors (in attached .ai file), Embossment of logo/name/etc, thick card stock, colored borders (on card sides, not front/back faces)
Should not have
• Should not be bland, or unsexy.

```html
<!DOCTYPE html>
<html lang="en">
<head>
<meta charset="utf-8">
<title>Quillon Laboratories Business Card</title>
<link rel="stylesheet" href="https://fonts.googleapis.com/css2?family=Open+Sans:wght@300;400;600;700&display=swap">
<style>
  :root {
    --backdrop: #2a2320;
    --card-black: #0c0c0c;
    --card-black-soft: #161616;
    --quillon-green: #52c2ad;
    --text-white: #f2f2f2;
    --text-grey: #4a4a4a;
    --edge-white: #e8e8e8;
  }
  * { margin: 0; padding: 0; box-sizing: border-box; }
  html, body {
    width: 1200px;
    height: 842px;
    overflow: hidden;
    background: var(--backdrop);
    font-family: "Open Sans", Arial, sans-serif;
  }
  .stage { position: relative; width: 1200px; height: 842px; }

  .card {
    position: absolute;
    top: 271px;
    width: 525px;
    height: 300px;
    background: linear-gradient(135deg, var(--card-black-soft), var(--card-black) 60%);
    overflow: hidden;
    box-shadow: 0 12px 30px rgba(0,0,0,.55);
  }
  .card--front { left: 50px; }
  .card--back  { left: 625px; }

  /* front */
  .band {
    position: absolute; left: 0; width: 100%; height: 14px;
    background: var(--quillon-green);
  }
  .band--top { top: 0; }
  .band--bottom { bottom: 0; }

  .wordmark {
    position: absolute;
    display: flex; align-items: center; gap: 16px;
  }
  .wordmark__square {
    width: 62px; height: 62px;
    border: 3px solid var(--text-white);
    flex: none;
  }
  .wordmark__text { line-height: 1; font-weight: 300; color: var(--text-white); }
  .wordmark__name { font-size: 44px; letter-spacing: 10px; display: block; }
  .wordmark__sub  { font-size: 19px; letter-spacing: 6.5px; display: block; margin-top: 6px; }

  .card--front .wordmark { left: 102px; top: 78px; }

  .person {
    position: absolute; right: 300px; top: 188px; text-align: right;
    color: var(--text-white);
  }
  .person__name { font-size: 17px; font-weight: 700; }
  .person__title { font-size: 14px; font-weight: 400; margin-top: 1px; }

  .contact {
    position: absolute; left: 253px; top: 166px;
    list-style: none; color: var(--text-white);
    font-size: 13.5px; line-height: 21px;
  }
  .contact li { display: flex; align-items: center; gap: 8px; }
  .contact svg { width: 11px; height: 11px; fill: var(--text-white); flex: none; }

  /* back */
  .edge-tab {
    position: absolute; width: 34px; height: 48px;
    background: var(--quillon-green);
  }
  .edge-tab::after {
    content: ""; position: absolute; top: 0; width: 5px; height: 100%;
    background: var(--edge-white);
  }
  .edge-tab--left { left: 0; top: 92px; }
  .edge-tab--left::after { right: 0; }
  .edge-tab--right { right: 0; top: 16px; }
  .edge-tab--right::after { left: 0; }

  .card--back .wordmark { left: 118px; top: 96px; }
  .card--back .wordmark__square {
    background: var(--quillon-green);
    border: 3px solid #2f2f2f;
  }
  .card--back .wordmark__text { color: var(--text-grey); }
  .card--back .wordmark__name { font-size: 40px; letter-spacing: 9px; }
  .card--back .wordmark__sub  { font-size: 17px; letter-spacing: 6px; }

  .services {
    position: absolute; left: 0; right: 0; top: 190px;
    text-align: center; color: var(--text-white);
    font-size: 14px; font-weight: 400; letter-spacing: .2px;
  }
</style>
</head>
<body>
<main class="stage">

  <section class="card card--front" aria-label="Business card front">
    <div class="band band--top"></div>
    <div class="wordmark">
      <span class="wordmark__square"></span>
      <span class="wordmark__text">
        <span class="wordmark__name">QUILLON</span>
        <span class="wordmark__sub">LABORATORIES</span>
      </span>
    </div>

    <div class="person">
      <p class="person__name">Jed Harlow</p>
      <p class="person__title">CEO</p>
    </div>

    <ul class="contact">
      <li>
        <svg viewBox="0 0 12 12"><path d="M3 0h6a1 1 0 0 1 1 1v10a1 1 0 0 1-1 1H3a1 1 0 0 1-1-1V1a1 1 0 0 1 1-1zm0 1.5v8h6v-8zM6 10.2a.6.6 0 1 0 0 1.2.6.6 0 0 0 0-1.2z"/></svg>
        484 562 0937
      </li>
      <li>
        <svg viewBox="0 0 12 12"><path d="M0 2h12v8H0zm1 1v.3l5 3.4 5-3.4V3zm0 1.5V9h10V4.5L6 8z"/></svg>
        JedH@quillorbit.example
      </li>
      <li>
        <svg viewBox="0 0 12 12"><circle cx="6" cy="6" r="5.5"/></svg>
        www.QuillOrbit.example
      </li>
    </ul>
    <div class="band band--bottom"></div>
  </section>

  <section class="card card--back" aria-label="Business card back">
    <div class="edge-tab edge-tab--left"></div>
    <div class="edge-tab edge-tab--right"></div>
    <div class="wordmark">
      <span class="wordmark__square"></span>
      <span class="wordmark__text">
        <span class="wordmark__name">QUILLON</span>
        <span class="wordmark__sub">LABORATORIES</span>
      </span>
    </div>
    <p class="services">Artificial Intelligence | Automation | Machine Learning</p>
  </section>

</main>
</body>
</html>
```